Modern Wind Energy Services Flyer VALTORA GmbH & Co. KG

We need a modern, high-quality and professional flyer design for a wind energy trade fair (Rotor Expo).

The flyer is intended to present our company VALTORA GmbH & Co. KG – a service company in the field of renewable energies with a focus on wind turbines.

The goal is to make a strong first impression on the following target groups:

OEMs
Wind farm operator
Service company
EPC Contractors

and to gain new collaborations.

🔹 FORMAT & LAYOUT

The flyer should be designed as a tri-fold flyer (6 pages).

6 panels (3 outside, 3 inside)
clear structure and good readability
The design must take the folds into account (no important content in the fold).
🔹 DESIGN STYLE
modern, clean, professional
high-quality corporate look
not overloaded (less text, more impact)
Powerful images (wind turbines, technicians, offshore/onshore)
Colors: Blue, white (optional subtle accents such as orange/sunset)

The flyer should appear international and high-quality, not like a local small business.

🔹 CONTENT – STRUCTURE (IMPORTANT)
🔹 FRONT SIDE

VALTORA
Progress Through Craft

Headline:
Wind Turbine Experts.
Delivered Worldwide.

Subline:
Maintenance · Retrofit · Blade Services · Access Solutions

Icons / short points:

Blade Repair
Rope Access
Mechanical Retrofit
Fast Mobilization
🔹 INSIDE (3 PAGES)**

About VALTORA
VALTORA delivers high-performance wind turbine services for OEMs, operators and EPC contractors.
Our teams operate in complex environments, combining technical expertise, advanced access solutions and fast mobilization worldwide.

Core Services

Maintenance & servicing
Major component replacement
Mechanical retrofits & upgrades
Complex repair works

Blade Solutions

External & internal inspections
Structural & leading edge repairs
Robotic internal blade inspection
Preventive maintenance

Access Capabilities

IRATA rope access
Blade platforms (KPB-4 / KPB-2)
Work at height in complex environments

Why VALTORA

Experienced in demanding projects
Fast & flexible deployment
Strong expertise in retrofit & repair
Reliable partner for long-term cooperation

Safety
Safety is our top priority.
All works are performed under strict HSE standards, RAMS procedures and Permit-to-Work systems.

🔹 BACK

VALTORA GmbH & Co. KG
Germany

+49 152 3961074
www.val-tora. de

🔹 IMPORTANT FOR DESIGNERS

Please design the flyer to be minimalist and high-quality.
Less text, clear structure and strong visual impact are crucial.

Target Market(s)

Wind turbine OEMs, wind farm operators, EPC contractors and service companies in the renewable energy sector worldwide

Industry/Entity Type

Renewable Energy / Wind Energy / Industrial Services

Font styles to use
Sans Serif

Colors
0054AA
0677BA
7BADD7
CADEEF
E8F1F8
0094D4
00A9DD
6FCCEA
C7EBF8
E9F6FB

Requirements
Must have
• Tri-fold brochure (6 panels) Clean, modern and premium design Strong front page with big headline and image Clear structure and easy readability Use of icons for services Professional wind energy images (turbines, technicians, offshore/onshore) Proper layout respecting folds (no important text in fold areas) High-quality, corporate look
Nice to have
• Subtle gradients (dark blue / energy style) Minimalistic and high-end layout Strong visual hierarchy (headline > sections > details) Modern icons and clean typography Balanced white space Slight premium / “big company” feeling (like large international energy companies)
Should not have
• Too much text or long paragraphs Overcrowded or messy layout Cheap or outdated design Clipart or low-quality images Too many colors Small unreadable fonts Generic “template-looking” designs

```html
<!DOCTYPE html>
<html lang="en">
<head>
<meta charset="utf-8">
<title>VALTORA – Wind Turbine Services Tri-fold</title>
<link rel="stylesheet" href="https://fonts.googleapis.com/css2?family=Barlow+Semi+Condensed:ital,wght@0,400;0,500;0,600;0,700;1,400;1,500;1,600&display=swap">
<style>
  :root {
    --navy: #0b3d7a;
    --blue-deep: #0054AA;
    --blue: #0677BA;
    --blue-soft: #7BADD7;
    --blue-pale: #CADEEF;
    --blue-mist: #E8F1F8;
    --slate-pale: #c9d6df;
    --sky: #C7EBF8;
    --ink: #2b3440;
    --white: #ffffff;
    --orange: #f6a11a;
    --stage: #e6e6e6;
    --font: "Barlow Semi Condensed", sans-serif;
  }
  * { box-sizing: border-box; margin: 0; padding: 0; }
  html, body { width: 1200px; height: 857px; overflow: hidden; }
  body { background: var(--stage); font-family: var(--font); color: var(--ink); position: relative; }

  .panel { position: absolute; top: 148px; width: 260px; height: 560px; overflow: hidden; }
  .spread { position: absolute; left: 60px; top: 148px; width: 780px; height: 560px; box-shadow: 0 14px 30px rgba(0,0,0,.18); }
  .spread .panel { top: 0; }
  .panel--core { left: 0; background: var(--blue-mist); }
  .panel--blade { left: 260px; background: #d3dee6; }
  .panel--why { left: 520px; background: var(--slate-pale); }
  .fold { position: absolute; top: 0; width: 1px; height: 100%; background: rgba(0,0,0,.07); }

  .section-band {
    position: absolute; left: 0; width: 100%; height: 36px;
    background: linear-gradient(90deg, var(--navy) 0%, var(--blue-deep) 45%, rgba(123,173,215,.4) 100%);
    color: var(--white); font-weight: 700; font-size: 22px; line-height: 36px; padding-left: 26px;
  }
  .bullets { position: absolute; left: 26px; right: 12px; list-style: none; }
  .bullets li { font-size: 14px; line-height: 26px; padding-left: 16px; position: relative; color: var(--ink); white-space: nowrap; }
  .bullets li::before { content: ""; position: absolute; left: 0; top: 10px; width: 6px; height: 6px; background: var(--blue-deep); }

  .photo { position: absolute; left: 0; width: 100%; }
  .photo--platform { top: 216px; height: 344px; background: linear-gradient(180deg, #b9d2ea 0%, #8fb0d9 40%, #6f94c9 100%); border-top: 3px solid var(--white); }
  .photo--field { top: 200px; height: 150px; background: linear-gradient(180deg, #c5d9ec 0%, #b7cde2 45%, #7d9f66 70%, #5f8e47 100%); border-top: 3px solid var(--white); border-bottom: 3px solid var(--white); }
  .photo--tower { top: 350px; height: 210px; background: linear-gradient(180deg, #7a9ed0 0%, #6a8fc5 100%); }

  .check-head { position: absolute; left: 24px; font-weight: 700; font-size: 22px; color: var(--blue-deep); }
  .checks { position: absolute; left: 24px; right: 12px; list-style: none; }
  .checks li { display: flex; gap: 8px; font-size: 13.5px; font-style: italic; line-height: 17px; margin-bottom: 8px; color: var(--ink); }
  .checks svg { flex: 0 0 12px; margin-top: 3px; }

  .safety { position: absolute; left: 0; bottom: 0; width: 100%; height: 180px; background: linear-gradient(160deg, #3a6aac 0%, var(--navy) 100%); color: var(--white); padding: 22px 24px; }
  .safety__head { display: flex; align-items: center; gap: 10px; font-weight: 700; font-size: 22px; }
  .safety__text { margin-top: 12px; font-size: 13.5px; font-style: italic; line-height: 19px; color: #dbe6f3; }

  .panel--cover { left: 890px; background: var(--white); box-shadow: 0 14px 30px rgba(0,0,0,.18); }
  .cover__brand { height: 118px; display: flex; flex-direction: column; align-items: center; justify-content: center; }
  .brand-name { font-weight: 700; font-size: 44px; color: var(--blue-deep); letter-spacing: 1px; line-height: 1; }
  .brand-tag { margin-top: 4px; font-size: 10.5px; letter-spacing: 2.6px; color: var(--blue-deep); text-transform: uppercase; }
  .cover__stripe { height: 8px; background: var(--sky); }
  .cover__hero { position: absolute; top: 126px; left: 0; width: 100%; height: 434px; background: linear-gradient(180deg, #1f4f92 0%, #3668a8 38%, #b8c8dc 54%, #5a7fb8 68%, #2a4f8f 100%); }
  .cover__copy { position: absolute; top: 144px; left: 18px; right: 10px; color: var(--white); }
  .headline { font-weight: 700; font-size: 36px; line-height: 35px; }
  .headline-accent { font-weight: 700; font-size: 24px; line-height: 28px; color: var(--orange); margin-top: 4px; }
  .subline { font-size: 13px; line-height: 17px; margin-top: 6px; }
  .features { position: absolute; left: 0; top: 382px; width: 100%; list-style: none; padding: 8px 0 8px 22px; background: linear-gradient(90deg, rgba(11,61,122,.75), rgba(11,61,122,.1)); }
  .features li { display: flex; align-items: center; gap: 14px; height: 40px; color: var(--white); font-weight: 700; font-size: 15px; }
  .features svg { width: 28px; height: 28px; flex: 0 0 28px; }
</style>
</head>
<body>

<section class="spread" aria-label="Inside spread">
  <div class="panel panel--core">
    <div class="section-band" style="top:26px">Core Services</div>
    <ul class="bullets" style="top:76px">
      <li>Maintenance &amp; Servicing</li>
      <li>Major Component Replacement</li>
      <li>Mechanical Retrofits &amp; Upgrades</li>
      <li>Complex Repair Works</li>
    </ul>
    <div class="photo photo--platform" role="img" aria-label="Photo of a blade platform with technicians suspended on a wind turbine tower against blue sky"></div>
  </div>

  <div class="panel panel--blade">
    <div class="section-band" style="top:26px">Blade Solutions</div>
    <ul class="bullets" style="top:76px">
      <li>External &amp; Internal Inspections</li>
      <li>Structural &amp; Leading Edge Repairs</li>
      <li>Robotic Internal Blade Inspection</li>
      <li>Preventive Maintenance</li>
    </ul>
    <div class="photo photo--field" role="img" aria-label="Photo of a blade access gondola high above green farmland"></div>
    <div class="photo photo--tower" role="img" aria-label="Photo of a white turbine tower against blue sky"></div>
  </div>

  <div class="panel panel--why">
    <div class="check-head" style="top:24px">Why VALTORA</div>
    <ul class="checks" style="top:62px">
      <li><svg viewBox="0 0 12 12" width="12" height="12"><circle cx="6" cy="6" r="5.2" fill="none" stroke="var(--blue-deep)" stroke-width="1.4"/><path d="M3.4 6.2l1.8 1.8 3.5-3.6" fill="none" stroke="var(--blue-deep)" stroke-width="1.5"/></svg>Proven in Demanding Projects</li>
      <li><svg viewBox="0 0 12 12" width="12" height="12"><circle cx="6" cy="6" r="5.2" fill="none" stroke="var(--blue-deep)" stroke-width="1.4"/><path d="M3.4 6.2l1.8 1.8 3.5-3.6" fill="none" stroke="var(--blue-deep)" stroke-width="1.5"/></svg>Fast &amp; Flexible Deployment</li>
      <li><svg viewBox="0 0 12 12" width="12" height="12"><circle cx="6" cy="6" r="5.2" fill="none" stroke="var(--blue-deep)" stroke-width="1.4"/><path d="M3.4 6.2l1.8 1.8 3.5-3.6" fill="none" stroke="var(--blue-deep)" stroke-width="1.5"/></svg>Strong Retrofit &amp; Repair Expertise</li>
      <li><svg viewBox="0 0 12 12" width="12" height="12"><circle cx="6" cy="6" r="5.2" fill="none" stroke="var(--blue-deep)" stroke-width="1.4"/><path d="M3.4 6.2l1.8 1.8 3.5-3.6" fill="none" stroke="var(--blue-deep)" stroke-width="1.5"/></svg>Reliable Long-Term Partner</li>
    </ul>
    <div class="check-head" style="top:192px">Access Capabilities</div>
    <ul class="checks" style="top:230px">
      <li><svg viewBox="0 0 12 12" width="12" height="12"><circle cx="6" cy="6" r="5.2" fill="none" stroke="var(--blue-deep)" stroke-width="1.4"/><path d="M3.4 6.2l1.8 1.8 3.5-3.6" fill="none" stroke="var(--blue-deep)" stroke-width="1.5"/></svg>IRATA Rope Access</li>
      <li><svg viewBox="0 0 12 12" width="12" height="12"><circle cx="6" cy="6" r="5.2" fill="none" stroke="var(--blue-deep)" stroke-width="1.4"/><path d="M3.4 6.2l1.8 1.8 3.5-3.6" fill="none" stroke="var(--blue-deep)" stroke-width="1.5"/></svg>Blade Platforms (KPB-4 / KPB-2)</li>
      <li><svg viewBox="0 0 12 12" width="12" height="12"><circle cx="6" cy="6" r="5.2" fill="none" stroke="var(--blue-deep)" stroke-width="1.4"/><path d="M3.4 6.2l1.8 1.8 3.5-3.6" fill="none" stroke="var(--blue-deep)" stroke-width="1.5"/></svg>Work at Height in<br>Complex Environments</li>
    </ul>
    <div class="safety">
      <div class="safety__head">
        <svg viewBox="0 0 30 34" width="30" height="34"><path d="M15 2l12 4.5v9c0 8-5.5 13.5-12 16-6.5-2.5-12-8-12-16v-9z" fill="rgba(255,255,255,.15)" stroke="var(--white)" stroke-width="1.8"/><path d="M9.5 17l4 4 7-8" fill="none" stroke="var(--white)" stroke-width="2"/></svg>
        SAFETY
      </div>
      <p class="safety__text">Safety is our top priority.<br>All work is performed under strict<br>HSE standards, RAMS procedures,<br>and Permit-to-Work systems.</p>
    </div>
  </div>

  <span class="fold" style="left:260px"></span>
  <span class="fold" style="left:520px"></span>
</section>

<section class="panel panel--cover" aria-label="Front cover">
  <div class="cover__brand">
    <span class="brand-name">VALTORA</span>
    <span class="brand-tag">Progress Through Craft</span>
  </div>
  <div class="cover__stripe"></div>
  <div class="cover__hero" role="img" aria-label="Photo of a turbine blade above the clouds with a technician on the nacelle"></div>
  <div class="cover__copy">
    <h1 class="headline">Wind Turbine<br>Experts.</h1>
    <p class="headline-accent">Delivered Worldwide.</p>
    <p class="subline">• Maintenance &nbsp;• Retrofit<br>• Blade Services &nbsp;• Access Solutions</p>
  </div>
  <ul class="features">
    <li><svg viewBox="0 0 28 28"><path d="M4 22L18 8M15 5l8 8M6 24l-2-2" fill="none" stroke="#fff" stroke-width="1.8"/><circle cx="20" cy="6" r="2.5" fill="none" stroke="#fff" stroke-width="1.6"/></svg>Blade Repair</li>
    <li><svg viewBox="0 0 28 28"><path d="M14 2v10" stroke="#fff" stroke-width="1.8"/><circle cx="14" cy="15" r="3" fill="none" stroke="#fff" stroke-width="1.8"/><path d="M14 18v8M9 22h10" stroke="#fff" stroke-width="1.8"/></svg>Rope Access</li>
    <li><svg viewBox="0 0 28 28"><circle cx="14" cy="14" r="5" fill="none" stroke="#fff" stroke-width="1.8"/><path d="M14 3v4M14 21v4M3 14h4M21 14h4M6.2 6.2l2.8 2.8M19 19l2.8 2.8M6.2 21.8L9 19M19 9l2.8-2.8" stroke="#fff" stroke-width="1.8"/></svg>Mechanical Retrofit</li>
    <li><svg viewBox="0 0 28 28"><rect x="2" y="9" width="15" height="11" rx="1.5" fill="none" stroke="#fff" stroke-width="1.8"/><path d="M17 12h5l4 4v4h-9" fill="none" stroke="#fff" stroke-width="1.8"/><circle cx="8" cy="22" r="2.3" fill="var(--navy)" stroke="#fff" stroke-width="1.6"/><circle cx="21" cy="22" r="2.3" fill="var(--navy)" stroke="#fff" stroke-width="1.6"/></svg>Fast Mobilization</li>
  </ul>
</section>

</body>
</html>
```